Get me out of Jail business cards!!!!

I need business cards done for my business. I own a BailBonds and I get people out of jail!

Colors are red white and black

I need it to say on the card these details:

Rollin’ Free Bailbonds

452 S Kettering Ave
Cedar Hollow, FL 34901

863-555-0172

Open 24/7

On the back of the card:

Must check in every Tuesday.

______/______/______ court date
____________________ time
You must know your court date at all times!

Marla Tisdell - owner
Rosalind Tisdell - agent
Denise Crandon - agent

Industry/Entity Type

Bail bonds

Contact Information for Business Card

Colors are red white and black I need it to say on the card these details: Rollin’ Free Bailbonds 452 S Kettering Ave Cedar Hollow, FL 34901 863-555-0172 Open 24/7 On the back of the card: Must check in every Tuesday. ______/______/______ court date ____________________ time You must know your court date at all times! Marla Tisdell - owner Rosalind Tisdell - agent Denise Crandon - agent

Font styles to use
Serif
Sans Serif

Colors
EB3D1F
EC4F4E
F09395
F8D3D4
FCEDEE

Requirements
Must have
• I listed the must haves in the business card details
Nice to have
• Handcuffs or jail bars or a man in a black and white suit

```html
<!DOCTYPE html>
<html lang="en">
<head>
<meta charset="utf-8">
<title>Rollin’ Free Bailbonds – Business Cards</title>
<link rel="stylesheet" href="https://fonts.googleapis.com/css2?family=Questrial&family=Arimo:wght@400;700&display=swap">
<style>
  :root {
    --bg: #e6e5e2;
    --ink: #222226;
    --red: #f00a0a;
    --white: #ffffff;
    --line: #333338;
    --cuff-dark: #141417;
    --cuff-mid: #3a3a40;
  }
  * { box-sizing: border-box; margin: 0; padding: 0; }
  html, body { width: 1200px; height: 801px; overflow: hidden; }
  body {
    background: var(--bg);
    font-family: "Arimo", Arial, sans-serif;
    position: relative;
  }
  .card {
    position: absolute;
    top: 246px;
    width: 540px;
    height: 309px;
    overflow: hidden;
    box-shadow: 0 6px 18px rgba(0,0,0,.18);
  }
  .wordmark {
    font-family: "Questrial", "Helvetica Neue", sans-serif;
    font-weight: 400;
    letter-spacing: .5px;
    white-space: nowrap;
  }

  /* Front */
  .card-front {
    left: 40px;
    background: var(--ink);
    border-bottom: 4px solid var(--red);
  }
  .card-front .wordmark {
    position: absolute;
    left: 30px; top: 40px;
    font-size: 46px;
    line-height: 1;
    color: var(--white);
  }
  .handcuff-art {
    position: absolute;
    right: 24px; top: 106px;
    width: 200px; height: 170px;
    border-radius: 80px;
    background: radial-gradient(ellipse at 60% 40%, var(--cuff-mid), var(--cuff-dark) 75%);
    opacity: .9;
  }
  .contact {
    position: absolute;
    left: 34px; bottom: 32px;
    color: var(--white);
    font-size: 14px;
    line-height: 1.4;
  }
  .contact .hours span { color: var(--red); }
  .contact .phone { display: flex; align-items: center; gap: 6px; margin-bottom: 14px; }
  .contact .phone svg { width: 12px; height: 12px; }

  /* Back */
  .card-back {
    left: 620px;
    background: var(--white);
    border-bottom: 4px solid var(--red);
  }
  .card-back .wordmark {
    position: absolute;
    right: 28px; top: 24px;
    font-size: 42px;
    line-height: 1;
    color: var(--ink);
  }
  .checkin {
    position: absolute;
    left: 30px; top: 86px;
    color: var(--red);
    font-size: 15px;
  }
  .fill-row {
    position: absolute;
    left: 30px;
    display: flex;
    align-items: flex-end;
    gap: 8px;
    font-size: 15px;
    color: var(--line);
  }
  .fill-row .blank { display: inline-block; border-bottom: 1px solid var(--line); height: 16px; }
  .row-date { top: 118px; }
  .row-time { top: 150px; }
  .notice-band {
    position: absolute;
    left: 0; right: 0; top: 190px;
    height: 30px;
    background: var(--red);
    color: var(--white);
    font-size: 16px;
    line-height: 30px;
    padding-left: 30px;
  }
  .staff {
    position: absolute;
    left: 0; right: 0; top: 220px; bottom: 0;
    background: var(--ink);
    display: flex;
    justify-content: space-between;
    padding: 16px 30px 0;
  }
  .staff-member .name { color: var(--red); font-weight: 700; font-size: 15px; }
  .staff-member .role { color: var(--white); font-size: 14px; margin-top: 2px; }
</style>
</head>
<body>

<section class="card card-front" aria-label="Business card front">
  <h1 class="wordmark">Rollin’ Free Bailbonds</h1>
  <div class="handcuff-art" role="img" aria-label="Embossed handcuffs illustration"></div>
  <div class="contact">
    <p class="hours">Open <span>24/7</span></p>
    <p class="phone">
      <svg viewBox="0 0 24 24" aria-hidden="true"><path fill="#f00a0a" d="M6.6 10.8a15 15 0 0 0 6.6 6.6l2.2-2.2a1 1 0 0 1 1-.25 11.4 11.4 0 0 0 3.6.57 1 1 0 0 1 1 1V20a1 1 0 0 1-1 1A17 17 0 0 1 3 4a1 1 0 0 1 1-1h3.5a1 1 0 0 1 1 1c0 1.25.2 2.45.57 3.57a1 1 0 0 1-.25 1z"/></svg>
      863-555-0172
    </p>
    <p class="address">452 S Kettering Ave<br>Cedar Hollow, FL 34901</p>
  </div>
</section>

<section class="card card-back" aria-label="Business card back">
  <h2 class="wordmark">Rollin’ Free Bailbonds</h2>
  <p class="checkin">Must check in every Tuesday.</p>
  <div class="fill-row row-date">
    <span class="blank" style="width:60px"></span>/<span class="blank" style="width:60px"></span>/<span class="blank" style="width:60px"></span>
    <span>court date</span>
  </div>
  <div class="fill-row row-time">
    <span class="blank" style="width:200px"></span>
    <span>time</span>
  </div>
  <p class="notice-band">You must know your court date at all times!</p>
  <div class="staff">
    <div class="staff-member"><p class="name">Marla Tisdell</p><p class="role">Owner</p></div>
    <div class="staff-member"><p class="name">Rosalind Tisdell</p><p class="role">Agent</p></div>
    <div class="staff-member"><p class="name">Denise Crandon</p><p class="role">Agent</p></div>
  </div>
</section>

</body>
</html>
```